New Website for novelty yarn producer

We need a new website for our company, Tarvek. We make highly tailored yarns for weavers worldwide. This year marks our 40th anniversary and we want to evolve our image and identity.

Our temporary website can be found at:
www.tarvekyarns.com

Our only concern in that throughout the website the protagonist must be our client, we make their creations possible and are highly adaptable both during the ideation process of the yarn as well as in the production. This is at the core of the way we do business and is summarised within the concept of FPM (Fluid Partner Method).

Industry/Entity Type

Textile

Number of Pages Required

1 page

Colors
9bcb3c

Requirements
Must have
• Fluid Partner Method (FPM) - can be found on or current website www.tarvekyarns.com

```html
<!DOCTYPE html>
<html lang="en">
<head>
<meta charset="utf-8">
<title>Tarvek — Yarn solutions for weavers</title>
<link rel="stylesheet" href="https://fonts.googleapis.com/css2?family=Lato:wght@300;400;700&display=swap">
<style>
  :root {
    --green: #5aae3f;
    --brand: #9bcb3c;
    --ink: #444444;
    --muted: #6a6a6a;
    --paper: #ffffff;
    --soft: #f6f6f6;
    --white: #ffffff;
  }
  * { box-sizing: border-box; margin: 0; padding: 0; }
  html, body { width: 836px; height: 1200px; overflow: hidden; }
  body { font-family: "Lato", sans-serif; background: var(--paper); color: var(--ink); position: relative; }

  .hero {
    position: absolute; left: 0; top: 0; width: 836px; height: 410px; overflow: hidden;
    background: linear-gradient(90deg, #0c0f12 0%, #12212c 12%, #1d4256 22%, #2d5a58 30%, #6a6a1a 38%, #c9a90f 44%, #e4c312 48%, #b86a2a 52%, #c0642e 56%, #8e1d1a 62%, #5a1414 68%, #6a5a55 74%, #3a3230 82%, #141212 92%, #0a0a0a 100%);
  }
  .hero::after {
    content: ""; position: absolute; inset: 0;
    background: linear-gradient(180deg, rgba(0,0,0,0.35) 0%, rgba(0,0,0,0.1) 40%, rgba(0,0,0,0.45) 100%);
  }
  .hero > * { position: absolute; z-index: 1; }
  .brand { left: 92px; top: 16px; color: var(--white); font-size: 18px; font-weight: 400; letter-spacing: 1px; }
  .nav { top: 21px; left: 0; width: 836px; height: 12px; }
  .nav a { position: absolute; color: var(--white); font-size: 8.5px; text-decoration: none; letter-spacing: 0.2px; }
  .slider-dots { left: 792px; top: 158px; width: 12px; height: 95px; }
  .dot { position: absolute; left: 1px; width: 9px; height: 9px; border: 1px solid var(--white); border-radius: 50%; }
  .dot.active::after { content: ""; position: absolute; left: 2px; top: 2px; width: 3px; height: 3px; background: var(--white); border-radius: 50%; }
  .dot-link { position: absolute; left: 5px; width: 1px; border-left: 1px dotted rgba(255,255,255,0.7); height: 18px; }
  .hero-title { left: 93px; top: 276px; color: var(--white); font-size: 25.5px; font-weight: 400; }
  .hero-sub { left: 93px; top: 312px; width: 460px; color: var(--white); font-size: 13.5px; line-height: 16px; }
  .hero-cta { left: 93px; top: 358px; color: var(--white); font-size: 8.5px; font-weight: 700; letter-spacing: 0.3px; display: flex; align-items: center; gap: 6px; }

  .offer { position: absolute; left: 0; top: 410px; width: 836px; height: 336px; background: var(--soft); }
  .offer-title { position: absolute; top: 62px; width: 100%; text-align: center; font-size: 21.5px; font-weight: 400; color: var(--ink); }
  .offer-rule { position: absolute; top: 90px; left: 384px; width: 75px; height: 1px; background: var(--green); }
  .service { position: absolute; top: 134px; width: 220px; margin-left: -110px; text-align: center; }
  .service-icon { width: 60px; height: 60px; border-radius: 50%; background: var(--green); margin: 0 auto; display: flex; align-items: center; justify-content: center; }
  .service-name { margin-top: 10px; font-size: 13.5px; color: var(--ink); font-weight: 400; }
  .service-text { margin-top: 6px; font-size: 9.6px; line-height: 14.8px; color: var(--muted); font-weight: 400; white-space: nowrap; }

  .feature { position: absolute; left: 0; width: 836px; height: 227px; }
  .feature.method { top: 746px; }
  .feature.production { top: 973px; }
  .feature-photo { position: absolute; top: 0; width: 418px; height: 100%; }
  .photo-weave { left: 0; background: radial-gradient(ellipse at 40% 40%, #3a5a8a 0%, #2a3a5a 40%, #6a6068 75%, #a89a88 100%); }
  .photo-mesh { left: 418px; background: linear-gradient(120deg, #3a2e22 0%, #8a7458 35%, #c8b698 50%, #6e5a42 70%, #2a2018 100%); }
  .feature-title { position: absolute; font-size: 21px; font-weight: 400; color: var(--ink); }
  .feature-text { position: absolute; font-size: 11.2px; line-height: 18.4px; color: var(--muted); }
  .method .feature-title { left: 451px; top: 60px; }
  .method .feature-text { left: 451px; top: 96px; width: 300px; }
  .production .feature-title { left: 93px; top: 68px; }
  .production .feature-text { left: 93px; top: 103px; width: 290px; }
</style>
</head>
<body>
  <header class="hero" role="img" aria-label="Close-up photograph of hanging textile drapes in blue, yellow, orange and red">
    <div class="brand">TARVEK</div>
    <nav class="nav">
      <a style="left:400px">HOME</a>
      <a style="left:454px">FLUID PARTNER METHOD</a>
      <a style="left:597px">ABOUT</a>
      <a style="left:654px">BLOG</a>
      <a style="left:703px">CONTACT</a>
    </nav>
    <div class="slider-dots">
      <span class="dot active" style="top:0"></span>
      <span class="dot-link" style="top:12px"></span>
      <span class="dot" style="top:42px"></span>
      <span class="dot-link" style="top:54px"></span>
      <span class="dot" style="top:83px"></span>
    </div>
    <h1 class="hero-title">Providing Outstanding Textiles For 40 Years</h1>
    <p class="hero-sub">Our team has decades of experience in providing yarn solutions to weavers around the world</p>
    <a class="hero-cta">LEARN MORE
      <svg width="10" height="7" viewBox="0 0 10 7"><path d="M0 3.5H9M6 0.5L9 3.5L6 6.5" stroke="#fff" fill="none" stroke-width="1"/></svg>
    </a>
  </header>

  <section class="offer">
    <h2 class="offer-title">What We Offer</h2>
    <div class="offer-rule"></div>

    <div class="service" style="left:198px">
      <div class="service-icon">
        <svg width="26" height="26" viewBox="0 0 26 26" fill="#fff" stroke="#fff" stroke-width="1.4">
          <circle cx="13" cy="13" r="3.2"/>
          <line x1="13" y1="13" x2="13" y2="4"/><line x1="13" y1="13" x2="21" y2="9"/>
          <line x1="13" y1="13" x2="20" y2="20"/><line x1="13" y1="13" x2="6" y2="20"/><line x1="13" y1="13" x2="4" y2="11"/>
          <circle cx="13" cy="4" r="1.8"/><circle cx="21" cy="9" r="1.8"/><circle cx="20" cy="20" r="1.8"/><circle cx="6" cy="20" r="1.8"/><circle cx="4" cy="11" r="1.8"/>
        </svg>
      </div>
      <h3 class="service-name">Network</h3>
      <p class="service-text">A network of weavers, yarn producers and<br>representatives consolidated over 40 years<br>of successful business operations.</p>
    </div>

    <div class="service" style="left:418px">
      <div class="service-icon">
        <svg width="26" height="26" viewBox="0 0 26 26" fill="none" stroke="#fff" stroke-width="1.4">
          <circle cx="8" cy="8" r="4.5"/><path d="M8 5.5V8H10"/>
          <rect x="9" y="11" width="9" height="8" fill="#fff"/>
          <path d="M18 13H21L23 16V19H18Z" fill="#fff"/>
          <circle cx="12" cy="20.5" r="1.6" fill="#5aae3f"/><circle cx="20" cy="20.5" r="1.6" fill="#5aae3f"/>
        </svg>
      </div>
      <h3 class="service-name">Logistics</h3>
      <p class="service-text">With a distribution grid organized<br>and tuned to perfection, we bring your yarns<br>where you need them, when you need them</p>
    </div>

    <div class="service" style="left:638px">
      <div class="service-icon">
        <svg width="26" height="26" viewBox="0 0 26 26" fill="#fff">
          <path d="M4 21V13L9 10V13L14 10V13L19 10V5H21V21Z"/>
          <rect x="7" y="16" width="2" height="2" fill="#5aae3f"/><rect x="11" y="16" width="2" height="2" fill="#5aae3f"/><rect x="15" y="16" width="2" height="2" fill="#5aae3f"/>
        </svg>
      </div>
      <h3 class="service-name">Production</h3>
      <p class="service-text">Production line is dynamic and solid,<br>allowing for freedom as well as<br>precision in any project</p>
    </div>
  </section>

  <section class="feature method">
    <div class="feature-photo photo-weave" role="img" aria-label="Macro photograph of a blue and cream woven yarn fabric"></div>
    <h2 class="feature-title">Fluid Partner Method</h2>
    <p class="feature-text">We believe that the key to delivering a yarn that exceeds our client's expectation is to work together with weavers from step one, starting from the desired end product and working backwards.</p>
  </section>

  <section class="feature production">
    <h2 class="feature-title">Production built around you</h2>
    <p class="feature-text">Versatility and flexibility both in development and production are key in delivering a custom solution capable of giving life to your products.</p>
    <div class="feature-photo photo-mesh" role="img" aria-label="Macro photograph of a golden braided yarn mesh"></div>
  </section>
</body>
</html>
```